Discreet simple classy for adult entertainment

I would like a matte black business card with gold writing for my business. Keeping it simple. Having my following:

Lana frost
Events. Entertainment. Promotions
0491726580

or alternatively could have what i had on my previous card below but i think i prefer the above as again - discretion.

Maybe a nice gold line thru the card or some other very simple design . Or not open to ideas/ can be doublesided if any good ideas with that.

included pics of my old bus card. not sure weather i want a photo on it or not. if i do it wont be the same pic. i kinda wanted a card that was discreet so if it was in someones wallet they wouldn't neccessarily realise it was from a stripper.

Target Market(s)

men

Industry/Entity Type

Business

Contact Information for Business Card

Lana frost
0491726580

Requirements
Nice to have
• i don't know i am really open to anything. im giving my cards to guys so something they can have in their wallet that is discreet preferably.

```html
<!DOCTYPE html>
<html lang="en">
<head>
<meta charset="utf-8">
<title>Lana Frost – Business Card</title>
<link rel="stylesheet" href="https://fonts.googleapis.com/css2?family=Cinzel:wght@400&family=EB+Garamond:wght@400&display=swap">
<style>
  :root {
    --page-bg: #e6e6e6;
    --card-white: #ffffff;
    --pattern-light: #f4f4f4;
    --pattern-mid: #dcdcdc;
    --panel-black: #000000;
    --panel-sheen: #1c1c1c;
    --ink-white: #ffffff;
  }
  html, body {
    margin: 0;
    padding: 0;
    width: 1200px;
    height: 884px;
    overflow: hidden;
    background: var(--page-bg);
  }
  .canvas {
    position: relative;
    width: 1200px;
    height: 884px;
  }
  .card {
    position: absolute;
    left: 80px;
    top: 172px;
    width: 1040px;
    height: 540px;
    background: var(--card-white);
    box-shadow: 0 10px 30px rgba(0,0,0,0.18);
    overflow: hidden;
  }
  .card-pattern {
    position: absolute;
    inset: 0;
    background: linear-gradient(180deg, var(--pattern-light) 0%, var(--card-white) 45%, var(--pattern-mid) 100%);
  }
  .info-panel {
    position: absolute;
    left: 153px;
    top: 88px;
    width: 658px;
    height: 368px;
    border-radius: 32px;
    background: linear-gradient(180deg, var(--panel-black) 0%, var(--panel-black) 45%, var(--panel-sheen) 58%, var(--panel-black) 75%);
    color: var(--ink-white);
    text-align: center;
  }
  .brand-name {
    position: absolute;
    left: 0;
    right: 0;
    top: 76px;
    margin: 0;
    font-family: "Cinzel", serif;
    font-weight: 400;
    font-size: 58px;
    letter-spacing: 2px;
    line-height: 1;
  }
  .tagline {
    position: absolute;
    left: 0;
    right: 0;
    top: 150px;
    margin: 0;
    font-family: "Cinzel", serif;
    font-size: 18px;
    letter-spacing: 0.5px;
    line-height: 1;
  }
  .divider {
    position: absolute;
    left: 244px;
    top: 200px;
    width: 170px;
    height: 6px;
  }
  .phone {
    position: absolute;
    left: 0;
    right: 0;
    top: 238px;
    margin: 0;
    font-family: "EB Garamond", serif;
    font-size: 31px;
    letter-spacing: 1px;
    line-height: 1;
  }
</style>
</head>
<body>
  <div class="canvas">
    <div class="card">
      <div class="card-pattern" role="img" aria-label="Light grey geometric diamond pattern covering the card face"></div>
      <div class="info-panel">
        <h1 class="brand-name">LANA FROST</h1>
        <p class="tagline">EVENTS. ENTERTAINMENT. PROMOTIONS</p>
        <svg class="divider" viewBox="0 0 170 6" aria-hidden="true">
          <path d="M0 3 L85 1.2 L170 3 L85 4.8 Z" fill="#ffffff"/>
        </svg>
        <p class="phone">0491726580</p>
      </div>
    </div>
  </div>
</body>
</html>
```